Business Card / Appointment Card for Physician

On one side it should give the logo, address, and contact information, and on the other side it should br an Appointment card.

One Side:
Logo (see attached files)
Board Certified American Orthopedic Surgery

1487 Harrowgate Ave.
Suite KM7
Bronx, NY 10527
Tel: (718) 552 - 1948
Fax: (718) 552 - 7210

628 Fourth Ave.
Suite 42
New York, NY 10087
Tel: (212) 734 - 2815

Second Side:
Appointment
give them a choice of Bronx or Mahattan office
For:
Date:
Time:

If you are unable to keep your appointment, please call (718) 263-5102 24hrs in advance.

Target Market(s)

People that need orthopedic surgery

Industry/Entity Type

Business

Contact Information for Business Card

smart and attractive

Requirements
Must have
• logo
• contact information on one side, appointment information on the other

```html
<!DOCTYPE html>
<html lang="en">
<head>
<meta charset="utf-8">
<title>Business and Appointment Card</title>
<link href="https://fonts.googleapis.com/css2?family=Didact+Gothic&display=swap" rel="stylesheet">
<style>
  :root {
    --backdrop: #e9e6e1;
    --card: #ffffff;
    --card-shade: #f1f3f5;
    --blue: #1f86c6;
    --blue-dark: #17679c;
    --green: #8cc152;
    --rule: #b9c0c7;
    --ink-soft: #5a6b78;
  }
  * { box-sizing: border-box; margin: 0; padding: 0; }
  html, body { width: 1200px; height: 780px; overflow: hidden; }
  body {
    background: var(--backdrop);
    font-family: "Didact Gothic", "Century Gothic", sans-serif;
    color: var(--blue);
    position: relative;
  }
  .card {
    position: absolute;
    background: linear-gradient(180deg, var(--card) 0%, var(--card-shade) 100%);
    border-radius: 22px;
    box-shadow: 0 10px 26px rgba(0,0,0,.18);
    overflow: hidden;
  }

  /* Front: contact side */
  .card-front { left: 90px; top: 90px; width: 340px; height: 595px; }
  .brand {
    padding-top: 58px;
    display: flex; flex-direction: column; align-items: center; gap: 10px;
  }
  .brand-mark { width: 40px; height: 40px; border-radius: 50%; background: var(--blue); }
  .brand-name { font-size: 21px; letter-spacing: .5px; text-align: center; }
  .brand-tagline { font-size: 11px; letter-spacing: .6px; text-transform: uppercase; }
  .office { text-align: center; margin-top: 30px; line-height: 1.32; font-size: 18px; }
  .office-title { font-size: 19px; font-weight: 400; margin-bottom: 2px; letter-spacing: .3px; }
  .contact-line { display: flex; justify-content: center; align-items: center; gap: 8px; }
  .contact-icon { width: 18px; height: 18px; flex: none; }
  .credential-band {
    position: absolute; left: 0; right: 0; bottom: 0; height: 96px;
    background: linear-gradient(180deg, var(--blue) 0%, var(--blue-dark) 100%);
    color: #fff; text-align: center; font-size: 17px; line-height: 1.35;
    display: flex; flex-direction: column; justify-content: center; letter-spacing: .6px;
  }

  /* Back: appointment side */
  .card-back { left: 510px; top: 210px; width: 595px; height: 340px; }
  .appointment-title { text-align: center; font-size: 28px; margin-top: 32px; letter-spacing: .4px; }
  .appointment-note { text-align: center; font-size: 15px; margin-top: 4px; }
  .appointment-form { margin: 28px 46px 0; font-size: 16px; color: var(--ink-soft); }
  .form-row { display: flex; align-items: flex-end; gap: 10px; margin-bottom: 26px; }
  .form-line { flex: 1; border-bottom: 1px solid var(--rule); height: 18px; }
  .form-line.short { flex: .7; }
  .meridiem { line-height: 1.1; font-size: 14px; }
  .reminder-band {
    position: absolute; left: 0; right: 0; bottom: 0; height: 40px;
    background: var(--blue); color: #fff; font-size: 13.5px;
    display: flex; align-items: center; justify-content: center; letter-spacing: .2px;
  }
</style>
</head>
<body>

<section class="card card-front" aria-label="Contact side">
  <header class="brand">
    <span class="brand-mark" aria-hidden="true"></span>
    <h1 class="brand-name">DANIEL R. WHITCOMBE MD PC</h1>
    <p class="brand-tagline">Orthopaedic Surgery &amp; Sports Medicine</p>
  </header>

  <div class="office">
    <h2 class="office-title">Bronx office</h2>
    <p>1487 Harrowgate Ave.</p>
    <p>Suite KM7</p>
    <p>Bronx, NY 10527</p>
    <p class="contact-line">
      <svg class="contact-icon" viewBox="0 0 20 20" aria-label="Telephone"><circle cx="10" cy="10" r="9.5" fill="var(--green)"/><path d="M6.5 5.5c.6-.5 1.3-.4 1.6.2l.8 1.6c.2.5 0 1-.4 1.3l-.6.4c.5 1.3 1.5 2.3 2.8 2.8l.4-.6c.3-.4.8-.6 1.3-.4l1.6.8c.6.3.7 1 .2 1.6-.8.9-2 1.1-3.1.6-2.3-1-4-2.7-5-5-.5-1.1-.3-2.3.6-3.1z" fill="#fff"/></svg>
      (718) 552 - 1948
    </p>
    <p class="contact-line">
      <svg class="contact-icon" viewBox="0 0 20 20" aria-label="Fax"><circle cx="10" cy="10" r="9.5" fill="var(--green)"/><rect x="7" y="4.5" width="6" height="4" fill="#fff"/><rect x="5" y="8" width="10" height="5.5" rx="1" fill="#fff"/><rect x="7" y="12" width="6" height="3.5" fill="#fff" stroke="var(--green)" stroke-width=".8"/></svg>
      (718) 552 - 7210
    </p>
  </div>

  <div class="office">
    <h2 class="office-title">Mahattan office</h2>
    <p>628 Fourth Ave.</p>
    <p>Suite 42</p>
    <p>New York, NY 10087</p>
    <p class="contact-line">
      <svg class="contact-icon" viewBox="0 0 20 20" aria-label="Telephone"><circle cx="10" cy="10" r="9.5" fill="var(--green)"/><path d="M6.5 5.5c.6-.5 1.3-.4 1.6.2l.8 1.6c.2.5 0 1-.4 1.3l-.6.4c.5 1.3 1.5 2.3 2.8 2.8l.4-.6c.3-.4.8-.6 1.3-.4l1.6.8c.6.3.7 1 .2 1.6-.8.9-2 1.1-3.1.6-2.3-1-4-2.7-5-5-.5-1.1-.3-2.3.6-3.1z" fill="#fff"/></svg>
      (212) 734 - 2815
    </p>
  </div>

  <footer class="credential-band">
    <span>Board Certified</span>
    <span>American Orthopedic Surgery</span>
  </footer>
</section>

<section class="card card-back" aria-label="Appointment side">
  <h2 class="appointment-title">Appointment</h2>
  <p class="appointment-note">give them a choice of Bronx or Mahattan office</p>

  <div class="appointment-form">
    <div class="form-row"><span>For:</span><span class="form-line"></span></div>
    <div class="form-row">
      <span>Date:</span><span class="form-line"></span>
      <span>Time:</span><span class="form-line short"></span>
      <span class="meridiem">am.<br>pm.</span>
    </div>
  </div>

  <footer class="reminder-band">If you are unable to keep your appointment, please call (718) 263-5102 24hrs in advance.</footer>
</section>

</body>
</html>
```